South Florida Real Estate Brokerage Business

The name is HOME CALVINA REAL ESTATE.
The company is a Real estate realty based in Miami.
Is targeted to Latin American clients.
Must express luxury, and efficiency.
Target clients for properties around 250k to a million +.
Calvina means Royal in Latin.
Should communicate safety and knowledge of the product and transaction with a tech edge.

The web design needs to be a Social tool, with Friendlane and other media integration of some sort. Needs to have a Show case place, a Search place (MLS listings) with maps and filters.
Needs to reflect luxury but also mixed with a social edge capable of engaging clients or transition them to communicate with the page.
Include the logo from the uploaded files, feel free to change the color or font per webdesign.
This is a Front en design, layout and graphics.
Possible future programming if approved.
I can receive Quotes for the Code part.

Target Market(s)

Spanish and English speakers living in Latin America and Canada looking for apartments and houses to buy.

Industry/Entity Type

Business

Requirements
Must have
• Search area.
Neighbourhood area.
Could be a blog or news area.
Client registration.
Social Plugin
Nice to have
• Social linking to networks.
Log in with friendlane account.
Friendlane Like.

```html
<!DOCTYPE html>
<html lang="en">
<head>
<meta charset="utf-8">
<title>Home Calvina Real Estate</title>
<link rel="stylesheet" href="https://fonts.googleapis.com/css2?family=Arimo:wght@400;700&family=Noto+Serif:wght@400;700&family=Cabin:wght@400;500&display=swap">
<style>
:root{
  --gold:#c9a766;
  --tan:#ecd6a0;
  --tan-row:#f0deb2;
  --light-row:#f2f0eb;
  --ink:#111;
  --grey-bg:#efefef;
  --footer:#353535;
  --footer-dark:#2a2a2a;
  --footer-text:#9a9a9a;
  --footer-accent:#c9c67a;
  --link:#3a4fc0;
}
*{box-sizing:border-box;margin:0;padding:0}
html,body{width:1200px;height:2528px;overflow:hidden}
body{position:relative;background:#fff;font-family:Arimo,Arial,sans-serif;color:var(--ink)}
.abs{position:absolute}

/* header */
.social-dots{left:126px;top:96px;display:flex;gap:10px}
.social-dots span{width:32px;height:32px;border-radius:50%;display:block}
.brand{left:490px;top:40px;width:240px;text-align:center}
.brand-mark{width:76px;height:60px;margin:0 auto 8px;background:var(--gold)}
.brand-name{font-family:"Noto Serif",serif;font-size:22px;font-weight:400;color:#3a3a3a;letter-spacing:1px;line-height:1.2}
.tools{left:922px;top:84px;display:flex}
.tools svg{width:56px;height:52px;border-left:2px solid #222;padding:6px}
.tools svg:last-child{border-right:2px solid #222}
.nav{left:0;top:165px;width:1200px;height:48px;display:flex;padding-left:141px;border-bottom:5px solid #ddd}
.nav a{font-weight:700;font-size:21px;color:#111;text-decoration:none;height:48px;line-height:48px;padding:0 13px;margin-right:26px}
.nav a.active{background:var(--gold);color:#111}

/* listings */
.listing{left:45px;width:660px;height:160px}
.listing .photo{position:absolute;left:0;top:0;width:204px;height:160px}
.listing h2{position:absolute;left:227px;top:2px;font-size:22px;letter-spacing:2.5px;text-decoration:underline;font-weight:700}
.listing p{position:absolute;left:227px;top:44px;font-size:14px;font-weight:700;line-height:28px;white-space:nowrap}
.read-more{position:absolute;left:483px;top:130px;width:100px;height:30px;background:#000;color:#fff;font-size:14px;font-weight:700;text-align:center;line-height:30px}

/* info table */
.info{left:727px;top:630px;width:428px;height:576px;background:var(--light-row)}
.info h3{font-family:"Noto Serif",serif;font-weight:700;font-size:21px;text-align:center;line-height:32px;padding-top:42px;height:125px;letter-spacing:.5px}
.info-row{display:flex;justify-content:space-between;height:35px;line-height:35px;padding:0 14px 0 16px;font-family:"Noto Serif",serif;font-size:15px}
.info-row:nth-child(odd){background:var(--tan-row)}
.info .more{display:block;text-align:right;padding:10px 14px 0 0;font-size:14px;font-weight:700;text-decoration:underline;color:#000}

/* strategies */
.section-title{font-size:28px;font-weight:700;letter-spacing:3px}
.strategy{width:330px}
.badge{position:absolute;left:0;top:0;width:60px;height:60px;border-radius:50%;background:radial-gradient(circle at 40% 35%,#f5e3b6,var(--gold) 70%);border:3px solid #e9dcc0;font-size:32px;font-weight:700;color:#333;text-align:center;line-height:54px}
.strategy h4{position:absolute;left:80px;top:4px;font-size:19px;line-height:22px}
.strategy p{position:absolute;left:0;top:66px;font-size:11.5px;font-weight:700;line-height:20px;letter-spacing:.8px;white-space:nowrap}
.agents-title{left:43px;top:1496px;font-size:21px;font-weight:700;text-decoration:underline}
.agent{width:320px;height:90px}
.agent .photo{position:absolute;left:0;top:0;width:82px;height:90px;border:2px solid #666}
.agent b{position:absolute;left:98px;top:18px;font-size:17px}
.agent span{position:absolute;left:98px;top:48px;font-size:17px;text-decoration:underline}

/* search */
.search{left:727px;top:1245px;width:428px;height:389px;background:var(--tan)}
.search h3{position:absolute;left:57px;top:20px;font-size:21px;letter-spacing:2.5px;line-height:27px}
.search label{position:absolute;font-size:16px;line-height:18px}
.search .field{position:absolute;height:27px;background:#fff;border:1px solid #777}
.search .go{position:absolute;left:280px;top:290px;width:92px;height:23px;background:#000;color:#fff;font-weight:700;font-size:14px;letter-spacing:1px;text-align:center;line-height:23px}
.search .hint{position:absolute;left:63px;top:324px;font-size:13px;letter-spacing:1.5px;line-height:22px}
.search .hint a{color:var(--link)}
.build{left:727px;top:1649px;width:428px;height:108px;background:linear-gradient(90deg,#e7cf92,#e9d7a8)}
.build svg{position:absolute;left:18px;top:6px}
.build p{position:absolute;left:166px;top:24px;font-size:27px;font-weight:700;letter-spacing:6px;line-height:30px}

/* map */
.locate{left:0;top:1780px;width:1200px;height:486px;background:var(--grey-bg)}
.locate h2{position:absolute;left:43px;top:24px}
.map{position:absolute;left:43px;top:77px;width:1114px;height:380px;background:linear-gradient(180deg,#a9c3dd 0%,#a9c3dd 38%,#e9e4d6 46%,#ece7d8 100%)}

/* footer */
.footer{left:0;top:2266px;width:1200px;height:262px;background:var(--footer);font-family:Cabin,sans-serif;color:var(--footer-text);font-size:14px}
.footer .col{position:absolute;top:50px}
.footer .col div{height:35px}
.footer .company{color:var(--footer-accent)}
.footer ul{list-style:none}
.footer li{height:35px;border-bottom:1px solid #444;width:140px}
.footer li::before{content:"•";margin-right:8px}
.footer .net{display:flex;align-items:center;gap:8px;height:35px}
.footer .net i{width:14px;height:14px;background:#8a8a8a;display:block}
.copy{position:absolute;left:757px;top:165px;width:295px;height:97px;background:var(--footer-dark);padding:30px 0 0 0;font-size:13px}
.copy b{display:block;color:#eee;font-weight:400;margin-top:10px}
</style>
</head>
<body>

<header>
  <div class="abs social-dots">
    <span style="background:#2f4f8a"></span><span style="background:#4a9fd8"></span><span style="background:#555"></span><span style="background:#e07a2a"></span>
  </div>
  <div class="abs brand">
    <div class="brand-mark"></div>
    <div class="brand-name">HOME CALVINA<br>REAL ESTATE</div>
  </div>
  <div class="abs tools">
    <svg viewBox="0 0 44 40" aria-label="Search"><circle cx="18" cy="17" r="10" fill="none" stroke="#111" stroke-width="3"/><line x1="25" y1="24" x2="36" y2="34" stroke="#111" stroke-width="4"/></svg>
    <svg viewBox="0 0 44 40" aria-label="Download"><rect x="8" y="14" width="24" height="20" fill="none" stroke="#111" stroke-width="2.5"/><path d="M22 4v18m-6-6 6 6 6-6" fill="none" stroke="#111" stroke-width="2.5"/></svg>
    <svg viewBox="0 0 44 40" aria-label="Mail"><rect x="4" y="9" width="36" height="24" fill="none" stroke="#111" stroke-width="2.5"/><path d="M4 9l18 14 18-14" fill="none" stroke="#111" stroke-width="2.5"/></svg>
    <svg viewBox="0 0 44 40" aria-label="Home"><path d="M6 20 22 6l16 14M10 17v17h24V17" fill="none" stroke="#111" stroke-width="2.5"/><rect x="18" y="24" width="8" height="10" fill="none" stroke="#111" stroke-width="2"/></svg>
  </div>
  <nav class="abs nav">
    <a class="active">Home</a><a>Building</a><a>Buying</a><a>Selling</a><a>Moving</a><a>Insurance</a><a>Contact Us</a>
  </nav>
</header>

<section class="abs showcase" style="left:0;top:272px;width:1200px;height:310px">
  <svg width="1200" height="310" viewBox="0 272 1200 310">
    <defs>
      <linearGradient id="mono" x1="0" y1="0" x2="0" y2="1"><stop offset="0" stop-color="#d9d9d9"/><stop offset=".6" stop-color="#8f8f8f"/><stop offset="1" stop-color="#5c5c5c"/></linearGradient>
      <linearGradient id="colour" x1="0" y1="0" x2="0" y2="1"><stop offset="0" stop-color="#7fb2e6"/><stop offset=".45" stop-color="#c9d8e6"/><stop offset=".7" stop-color="#9a8f82"/><stop offset="1" stop-color="#8b8b86"/></linearGradient>
    </defs>
    <polygon role="img" aria-label="Black and white photo of a modern building" points="45,282 194,310 194,557 45,580" fill="url(#mono)"/>
    <polygon role="img" aria-label="Black and white photo of an office block" points="189,310 387,338 387,540 189,551" fill="url(#mono)"/>
    <polygon role="img" aria-label="Black and white photo of a classic facade" points="821,330 1012,316 1012,535 821,540" fill="url(#mono)"/>
    <polygon role="img" aria-label="Black and white photo of a brick building" points="1008,312 1152,272 1152,580 1008,540" fill="url(#mono)"/>
    <rect role="img" aria-label="Photo of a glass office building under a blue sky" x="387" y="290" width="434" height="286" rx="6" fill="url(#colour)"/>
  </svg>
</section>

<section>
  <article class="abs listing" style="top:657px">
    <div class="photo" role="img" aria-label="Photo of a residential house at dusk" style="background:linear-gradient(160deg,#f0b04a,#b66a1c 60%,#6b4a22)"></div>
    <h2>RESIDENTIAL</h2>
    <p>Donec porta diam eu massa. Quisque diam lorem,<br>interdum vitae, dapibus ac, sceleri sque vitae,<br>pede. Donec eget tellus non erat lacinia fermentum.<br>Donec in velit vel ipsum</p>
    <span class="read-more">Read More</span>
  </article>
  <article class="abs listing" style="top:852px">
    <div class="photo" role="img" aria-label="Photo of a modern commercial building" style="background:linear-gradient(160deg,#7e8fc7,#c8c0b4 55%,#6d5d4c)"></div>
    <h2>COMMERCIAL</h2>
    <p>Donec porta diam eu massa. Quisque diam lorem,<br>interdum vitae, dapibus ac, sceleri sque vitae,<br>pede. Donec eget tellus non erat lacinia fermentum.<br>Donec in velit vel ipsum</p>
    <span class="read-more">Read More</span>
  </article>
  <article class="abs listing" style="top:1046px">
    <div class="photo" role="img" aria-label="Photo of a luxury villa courtyard at night" style="background:linear-gradient(160deg,#2d3550,#8a6a3a 55%,#b4945a)"></div>
    <h2>LUXURY</h2>
    <p>Donec porta diam eu massa. Quisque diam lorem,<br>interdum vitae, dapibus ac, sceleri sque vitae,<br>pede. Donec eget tellus non erat lacinia fermentum.<br>Donec in velit vel ipsum</p>
    <span class="read-more">Read More</span>
  </article>
</section>

<aside class="abs info">
  <h3>415 CORAL VISTA AVE, STE. 1200<br>MIAMI, FL 33137</h3>
  <div>
    <div class="info-row"><span>MLS#:</span><span>18700</span></div>
    <div class="info-row"><span>Status:</span><span>Active</span></div>
    <div class="info-row"><span>Price:</span><span>$1,600,500</span></div>
    <div class="info-row"><span>Bed/Bath:</span><span>6/5</span></div>
    <div class="info-row"><span>SQFT:</span><span>3210</span></div>
    <div class="info-row"><span>Year Built:</span><span>2012</span></div>
    <div class="info-row"><span>Lot Sizet:</span><span>3 Acres</span></div>
    <div class="info-row"><span>Garage:</span><span>2 Car Garage-Attached</span></div>
    <div class="info-row"><span>Roof:</span><span>Cedar Shake</span></div>
    <div class="info-row"><span>Heat:</span><span>Forced Air</span></div>
    <div class="info-row"><span>Taxes:</span><span>$25,020</span></div>
    <div class="info-row"><span>Exterior:</span><span>Stone, Stucco, Wood</span></div>
  </div>
  <a class="more">For More Information CLICK HERE</a>
</aside>

<section>
  <h2 class="abs section-title" style="left:43px;top:1248px">Real Estate Investment Strategies</h2>
  <div class="abs strategy" style="left:43px;top:1297px">
    <span class="badge">A</span><h4>Bargain<br>Purchase</h4>
    <p>Donec porta diam eu massa.<br>Quisque diam lorem,interdum<br>vitae, dapibus ac, sceleri sque<br>vitae, pede. Donec eget tellus<br>non erat lacinia fermentum.<br>Donec in velit vel ipsum</p>
  </div>
  <div class="abs strategy" style="left:395px;top:1297px">
    <span class="badge">B</span><h4>Increase<br>Value</h4>
    <p>Donec porta diam eu massa.<br>Quisque diam lorem,interdum<br>vitae, dapibus ac, sceleri sque<br>vitae, pede. Donec eget tellus<br>non erat lacinia fermentum.<br>Donec in velit vel ipsum</p>
  </div>

  <h2 class="abs agents-title">Our Agents</h2>
  <div class="abs agent" style="left:58px;top:1537px"><div class="photo" role="img" aria-label="Portrait of agent Marco Delaney" style="background:linear-gradient(#8a8f96,#5b5f66)"></div><b>Marco Delaney</b><span>Residential sales agent</span></div>
  <div class="abs agent" style="left:398px;top:1537px"><div class="photo" role="img" aria-label="Portrait of agent Rafael Ortun" style="background:linear-gradient(#6d5a44,#3f3428)"></div><b>Rafael Ortun</b><span>Real estate sales executive</span></div>
  <div class="abs agent" style="left:58px;top:1653px"><div class="photo" role="img" aria-label="Portrait of agent Lucia Arvelo" style="background:linear-gradient(#7c6a5a,#3a3430)"></div><b>Lucia Arvelo</b><span>Residential sales executive</span></div>
  <div class="abs agent" style="left:398px;top:1653px"><div class="photo" role="img" aria-label="Portrait of agent Nora Castell" style="background:linear-gradient(#a07a50,#4a3422)"></div><b>Nora Castell</b><span>Residential sales agent</span></div>
</section>

<form class="abs search">
  <h3>Residential Property<br>Search</h3>
  <label style="left:63px;top:81px">City &amp; State, or zip :</label>
  <span class="field" style="left:61px;top:101px;width:311px"></span>
  <label style="left:61px;top:130px">Search Area :</label>
  <span class="field" style="left:61px;top:150px;width:311px"></span>
  <label style="left:61px;top:178px">Price Range :</label>
  <label style="left:226px;top:178px">to :</label>
  <span class="field" style="left:61px;top:198px;width:147px"></span>
  <span class="field" style="left:226px;top:198px;width:146px"></span>
  <label style="left:61px;top:229px">Bedroom(s) :</label>
  <label style="left:226px;top:229px">Bathrooms :</label>
  <span class="field" style="left:61px;top:249px;width:147px"></span>
  <span class="field" style="left:226px;top:249px;width:146px"></span>
  <span class="go">Search</span>
  <p class="hint">Know exactly what you want? Try our<br><a>Advance Search</a></p>
</form>

<div class="abs build">
  <svg width="130" height="96" viewBox="0 0 130 96" aria-label="House badge">
    <polygon fill="#111" points="65,2 74,18 92,10 90,30 110,32 98,48 110,64 90,66 92,86 74,78 65,94 56,78 38,86 40,66 20,64 32,48 20,32 40,30 38,10 56,18"/>
    <path d="M47 50 65 34l18 16M52 47v19h26V47" fill="none" stroke="#e2c27a" stroke-width="4"/>
    <rect x="61" y="54" width="8" height="12" fill="#e2c27a"/>
  </svg>
  <p>Building<br>Your Home</p>
</div>

<section class="abs locate">
  <h2 class="section-title">Find Us Where We Are Locate</h2>
  <div class="map" role="img" aria-label="Street map showing the office location on the waterfront"></div>
</section>

<footer class="abs footer">
  <div class="col" style="left:140px">
    <div class="company">The Company Name Inc.</div>
    <div></div><div></div>
    <div style="height:22px">Freephone: +1 800 555 0147</div>
    <div style="height:22px">E-mail:</div>
    <div style="height:22px">Skype:</div>
  </div>
  <ul class="col" style="left:370px"><li>Site Map</li><li>News &amp; Info</li><li>Contact Us</li><li>Advertise With Us</li><li>Careers</li></ul>
  <ul class="col" style="left:562px"><li>Mortgage Rates</li><li>Trends Blog</li><li>Apartment Rentals</li><li>New Homes</li></ul>
  <div class="col" style="left:757px">
    <div class="net"><i></i>Chirpline</div>
    <div class="net"><i></i>Friendlane</div>
    <div class="net"><i></i>Tunelog</div>
  </div>
  <div class="col" style="left:908px">
    <div class="net"><i></i>Linkroster</div>
    <div class="net"><i></i>Tagshelf</div>
  </div>
  <div class="copy">© 2012 Real Estate. All Rights Reserved<b>Privacy Policy</b></div>
</footer>

</body>
</html>
```